Granite Mesa Auto Works web site for repairs,Parts, Accessories and Off Road

Need a wed site design for our light duty truck repair shop, also need to be able to sell our products from this page as well. Has our logo as the headliner and brief description of what we do and our history. An example of what we would want it to work like can be seen at www.kolbysgarage.com . This is a good example of style and accesses ability to buy parts we have.

Reason: needs more time and designs to come in

Target Market(s)

Light duty Diesel truck owners(Varnel,Brisco,Montavel)

Industry/Entity Type

Shop

Number of Pages Required

3 page

Font styles to use
Other font styles liked:
• The same font as our logo

Requirements
Must have
• A little about the shop and all of our services,availability to purchase our products, also a map of where we are located.
Nice to have
• I like the design of www.Kolbysgarage.com. Its easy to use and very descriptive of parts available

```html
<!DOCTYPE html>
<html lang="en">
<head>
<meta charset="utf-8">
<title>Granite Mesa Auto Works</title>
<link href="https://fonts.googleapis.com/css2?family=Montserrat:wght@400;500;600;700&display=swap" rel="stylesheet">
<style>
:root{
  --bg:#000000;
  --slate:#7486a8;
  --card:#2f3545;
  --link:#1a8cff;
  --white:#ffffff;
  --button:#0060c0;
  --ribbon:#ff8a00;
  --ink:#0a0a0a;
  --struck:#8a93a8;
}
*{margin:0;padding:0;box-sizing:border-box}
html,body{width:1200px;height:1000px;overflow:hidden;background:var(--bg)}
body{font-family:"Montserrat",sans-serif;color:var(--white);position:relative}
.testimonials{position:absolute;left:29px;top:52px;width:300px}
.testimonials h2{font-size:20px;font-weight:600;color:var(--slate);letter-spacing:.2px;margin-bottom:20px}
.quote{font-size:15.5px;font-weight:500;line-height:26px}
.author{font-size:15px;font-weight:500;color:var(--slate);margin:2px 0 26px}
.product{position:absolute;top:0;width:250px;height:224px;background:var(--card);border-radius:0 0 3px 3px;overflow:hidden}
.product .photo{position:absolute;left:10px;top:0;width:230px;height:125px;background:linear-gradient(180deg,#ffffff 0%,#f2f2f2 100%)}
.product .name{position:absolute;left:20px;top:140px;width:190px;font-size:14.5px;font-weight:500;line-height:21px;color:var(--link)}
.product .price{position:absolute;left:20px;top:190px;font-size:14.5px;font-weight:600}
.product .was{color:var(--struck);text-decoration:line-through;margin-right:12px;font-weight:500}
.ribbon{position:absolute;right:0;top:0;width:100px;height:100px}
.brands{position:absolute;left:370px;top:260px;width:800px;height:116px;background:var(--slate);border-radius:2px}
.brands h3{position:absolute;left:23px;top:24px;width:300px;font-size:17.5px;font-weight:700;line-height:23px}
.brands p{position:absolute;left:337px;top:22px;width:446px;font-size:14px;font-weight:500;line-height:24px;letter-spacing:-.1px}
.brands b{color:var(--ink);font-weight:600}
.contact{position:absolute;left:0;top:483px;width:1200px;height:380px;background:radial-gradient(ellipse at 55% 45%,#3a3a3a 0%,#262626 45%,#121212 100%)}
.contact .lead{position:absolute;top:108px;width:100%;text-align:center;font-size:19px;font-weight:500}
.contact .call{position:absolute;top:140px;width:100%;text-align:center;font-size:29px;font-weight:700;letter-spacing:.3px}
.contact .call span{color:var(--slate)}
.contact .or{position:absolute;top:214px;width:100%;text-align:center;font-size:15.5px;font-weight:600}
.email-btn{position:absolute;left:370px;top:245px;width:460px;height:50px;background:var(--button);border-radius:2px;display:flex;align-items:center;text-decoration:none;color:var(--white)}
.email-btn svg{margin-left:26px;margin-right:30px}
.email-btn span{font-size:15.5px;font-weight:500}
.footer{position:absolute;left:29px;right:31px;top:902px;display:flex;justify-content:space-between;font-size:14px;font-weight:500}
.footer nav a{color:var(--link);text-decoration:none}
.footer nav i{color:var(--link);font-style:normal;margin:0 11px}
.footer small{font-size:14px;color:var(--slate)}
</style>
</head>
<body>
<section class="testimonials">
  <h2>What our customers say</h2>
  <p class="quote">“Granite Mesa Auto Works are great, I really love them, their service is fantastic and they are great value for money.”</p>
  <p class="author">R J Calloway</p>
  <p class="quote">“Granite Mesa Auto Works are great, I really love them, their service is fantastic and they are great value for money.”</p>
  <p class="author">Dusty Trailhand</p>
</section>

<article class="product" style="left:370px">
  <div class="photo" role="img" aria-label="Product photo of LED light bars"></div>
  <p class="name">Product name in this space here</p>
  <p class="price">$400.00</p>
</article>
<article class="product" style="left:645px">
  <div class="photo" role="img" aria-label="Product photo of LED light bars"></div>
  <svg class="ribbon" viewBox="0 0 100 100">
    <polygon points="25,0 65,0 100,35 100,75" fill="var(--ribbon)"/>
    <text x="55" y="10" fill="#fff" font-family="Montserrat, sans-serif" font-weight="700" font-size="15" text-anchor="middle" dominant-baseline="central" transform="rotate(45 55 10)">REDUCED</text>
  </svg>
  <p class="name">Product name in this space here</p>
  <p class="price"><span class="was">$400.00</span>$295.00</p>
</article>
<article class="product" style="left:920px">
  <div class="photo" role="img" aria-label="Product photo of LED light bars"></div>
  <p class="name">Product name in this space here</p>
  <p class="price">$400.00</p>
</article>

<section class="brands">
  <h3>Granite Mesa Auto Works carries the lastest in truck performance tehnology!</h3>
  <p>We carry all the top selling brands like <b>K&amp;J Performance, TRVX, Sunridge Converters, JRL Tuning, Flo Max, QTR, Apex Diesel Engineering, Novaline diesel &amp; Many More!!</b></p>
</section>

<section class="contact" role="img" aria-label="Dim photo of a truck cab interior with leather seats and desert brush outside">
  <p class="lead">Can’t find what you’re looking for or need more info?</p>
  <p class="call">Give us a call on <span>(555) 014-2837</span></p>
  <p class="or">Or email us on</p>
  <a class="email-btn" href="#">
    <svg width="20" height="14" viewBox="0 0 20 14"><rect x="0.5" y="0.5" width="19" height="13" fill="#000" stroke="#000"/><polyline points="1,1 10,8 19,1" fill="none" stroke="#fff" stroke-width="1.2"/></svg>
    <span>enquiries@granitemesaautoworks.com</span>
  </a>
</section>

<footer class="footer">
  <nav><a href="#">Shipping Information</a><i>|</i><a href="#">Privacy Policy</a><i>|</i><a href="#">Testimonials</a><i>|</i><a href="#">Contact Us</a></nav>
  <small>© 2015 Granite Mesa Auto Works</small>
</footer>
</body>
</html>
```